Silver Fern Counseling business cards

Dana Korvath, LCPC, NCC
(410)555-0187
www.silverferncounseling.example
dana@silverferncounseling.example

Business cards. I would like it on the same background as pictured. Not on a white business card. I have attached the logo that was done by another designer with artflockly. I am open to looking at single-sided and double-sided designs.

Target Market(s)

teenagers and adults

Industry/Entity Type

mental health

Contact Information for Business Card

Dana Korvath, LCPC, NCC (410)555-0187 dana@silverferncounseling.example

Font styles to use
Other font styles liked:
• Cinzel

Colors

Designer to choose colors to be used in the design.

Requirements
Must have
• logo that is attached

```html
<!DOCTYPE html>
<html lang="en">
<head>
<meta charset="utf-8">
<title>Silver Fern Counseling – Business Cards</title>
<link rel="stylesheet" href="https://fonts.googleapis.com/css2?family=Montserrat:wght@400;500;600;700&display=swap">
<style>
  :root {
    --page-bg: #8a8a8a;
    --card-deep: #1b2a35;
    --card-mid: #2c3d4a;
    --card-light: #3d5060;
    --brand-teal: #7fb3c4;
    --text-light: #f2f5f7;
    --text-soft: #c9d3da;
    --rule: #a9b6bf;
  }
  * { box-sizing: border-box; margin: 0; padding: 0; }
  html, body { width: 1200px; height: 1015px; overflow: hidden; }
  body {
    background: var(--page-bg);
    font-family: "Montserrat", sans-serif;
    display: flex;
    flex-direction: column;
    align-items: center;
    justify-content: center;
    gap: 48px;
  }
  .card {
    position: relative;
    width: 760px;
    height: 434px;
    border-radius: 4px;
    overflow: hidden;
    box-shadow: 0 10px 28px rgba(0,0,0,0.35);
    display: flex;
    flex-direction: column;
    align-items: center;
    justify-content: center;
    color: var(--text-light);
  }
  .card-backdrop {
    position: absolute;
    inset: 0;
    background:
      radial-gradient(ellipse at 78% 35%, var(--card-light) 0%, transparent 55%),
      linear-gradient(160deg, var(--card-mid) 0%, var(--card-deep) 70%);
  }
  .card-content {
    position: relative;
    display: flex;
    flex-direction: column;
    align-items: center;
    text-align: center;
  }
  .brand {
    display: flex;
    align-items: center;
    gap: 14px;
  }
  .brand-dot {
    width: 22px;
    height: 22px;
    border-radius: 50%;
    background: var(--brand-teal);
  }
  .brand-name {
    font-weight: 600;
    font-size: 30px;
    letter-spacing: 0.06em;
    text-transform: uppercase;
    color: var(--brand-teal);
  }
  .website-front {
    margin-top: 56px;
    font-size: 19px;
    font-weight: 500;
    letter-spacing: 0.02em;
  }
  .contact-name {
    margin-top: 40px;
    font-size: 26px;
    font-weight: 700;
    letter-spacing: 0.04em;
    text-transform: uppercase;
  }
  .contact-name .credentials {
    font-size: 17px;
    font-weight: 600;
  }
  .contact-rule {
    width: 180px;
    height: 1px;
    background: var(--rule);
    margin: 12px 0 10px;
  }
  .contact-line {
    font-size: 18px;
    font-weight: 500;
    line-height: 1.5;
    color: var(--text-light);
  }
</style>
</head>
<body>
  <section class="card card-front">
    <div class="card-backdrop" role="img" aria-label="Soft blurred interior photograph in dark slate blue tones"></div>
    <div class="card-content">
      <div class="brand">
        <span class="brand-dot"></span>
        <span class="brand-name">Silver Fern Counseling</span>
      </div>
      <p class="website-front">www.silverferncounseling.example</p>
    </div>
  </section>

  <section class="card card-back">
    <div class="card-backdrop" role="img" aria-label="Soft blurred interior photograph in dark slate blue tones"></div>
    <div class="card-content">
      <div class="brand">
        <span class="brand-dot"></span>
        <span class="brand-name">Silver Fern Counseling</span>
      </div>
      <p class="contact-name">Dana Korvath, <span class="credentials">LCPC, NCC</span></p>
      <div class="contact-rule"></div>
      <p class="contact-line">(410)555-0187</p>
      <p class="contact-line">www.silverferncounseling.example</p>
      <p class="contact-line">dana@silverferncounseling.example</p>
    </div>
  </section>
</body>
</html>
```